Online Rug Store needs Clearance Banner

Website is: Lanternfield Carpets and Home
You can access it at: www.lanternfieldcarpetsandhome.com and login (top right) with password: trazok

*** update: When creating banners for my site, you have permission to use images from www.velbora.com, but ONLY for this project. The images/artwork are copyright allowable for use on www.lanternfieldcarpetsandhome.com projects.***

We need a home page banner sized 1000 wide x 500 tall pixels to promote a "Clearance Sale" on rugs. The banner can state:

1. Clearance Sale
2. Now in progress
3. Save an extra 20% with coupon code 'Mint20'
4. Ends March 31st
5. Plus Free Shipping and 30 day returns.

We prefer a banner that appears hand-drawn and artistic, not commercially produced. It is OK to use a room scene image, rug images, or just a colored/textured background with text and no images. Your choice.

Flat graphics with no shadows and 3-D effect preferred.
Attached is are 3 logo options, as well as an example banner with handcrafted, artistic styling that we prefer.

Target Market(s)

This should be an eye-catching banner to showcase a very urgent promotion. Consider using colors of red, white, gold, and black to make a strong statement on the home page.

Industry/Entity Type

Home And Garden

Requirements
Must have
• Winner must provide Photoshop editable file format (.psd format) including layers that can be edited.
Nice to have
• Hand-drawn, stenciled, scribbled, artistic graphics and fonts is nice because we sell rugs that are made by hand.
Should not have
• little to no shadowing. Avoid computerized graphics.

```html
<!DOCTYPE html>
<html lang="en">
<head>
<meta charset="utf-8">
<title>Lanternfield Carpets and Home</title>
<link href="https://fonts.googleapis.com/css2?family=Lora:wght@400&family=Cinzel:wght@400&family=Arimo:wght@400;700&family=Kaushan+Script&family=Permanent+Marker&display=swap" rel="stylesheet">
<style>
  :root {
    --frame: #000000;
    --page: #ffffff;
    --ink: #333333;
    --muted: #555555;
    --brand: #1c1c1c;
    --mark: #9b1c1f;
    --nav: #c8b28a;
    --field: #efece6;
    --banner-a: #b6a27f;
    --banner-b: #a48f6c;
    --sale-red: #8c2224;
    --white: #ffffff;
    --dot: #9aa3a8;
    --link: #8fa3b5;
    --card-line: #cfcfcf;
  }
  * { margin: 0; padding: 0; box-sizing: border-box; }
  html, body { width: 1200px; height: 1000px; overflow: hidden; background: var(--frame); }
  .page {
    position: absolute; left: 31px; top: 26px; width: 1138px; height: 948px;
    background: var(--page); overflow: hidden;
  }
  .brand { position: absolute; left: 102px; top: 70px; display: flex; align-items: center; gap: 14px; }
  .brand-square { width: 58px; height: 58px; background: var(--mark); }
  .brand-name {
    font-family: "Cinzel", serif; font-weight: 400; color: var(--brand);
    font-size: 22px; line-height: 28px; letter-spacing: 1px;
  }
  .account {
    position: absolute; right: 51px; top: 46px; text-align: right;
    font-family: "Arimo", sans-serif; font-size: 14px; color: var(--muted); line-height: 23px;
  }
  .account strong { color: var(--ink); font-weight: 700; }
  .search {
    position: absolute; left: 649px; top: 106px; width: 310px; height: 45px;
    background: var(--field); display: flex; align-items: center; justify-content: space-between;
    padding: 0 14px 0 10px; font-family: "Lora", serif; font-size: 15px; color: #8a8a8a;
  }
  .cart {
    position: absolute; left: 979px; top: 106px; width: 108px; height: 45px;
    background: var(--field); display: flex; align-items: center; justify-content: center; gap: 10px;
    font-family: "Lora", serif; font-size: 16px; color: var(--muted);
  }
  .nav {
    position: absolute; left: 0; top: 210px; width: 100%; height: 58px; background: var(--nav);
    display: flex; align-items: center; padding-left: 50px; gap: 35px;
    font-family: "Lora", serif; font-size: 17px; color: var(--white);
  }
  .hero {
    position: absolute; left: 50px; top: 299px; width: 1037px; height: 518px;
    background: radial-gradient(ellipse at center, var(--banner-a), var(--banner-b));
  }
  .hero-title {
    position: absolute; left: 0; top: 110px; width: 100%; text-align: center;
    font-family: "Kaushan Script", cursive; font-size: 128px; color: var(--sale-red); line-height: 1;
  }
  .hero-sub {
    position: absolute; left: 0; top: 345px; width: 100%; text-align: center;
    font-family: "Permanent Marker", cursive; font-size: 58px; color: var(--white); letter-spacing: 1px;
  }
  .hero-sub span { margin: 0 26px; font-size: 40px; vertical-align: 8px; }
  .hero-rule { position: absolute; left: 268px; top: 425px; }
  .dots { position: absolute; left: 0; top: 829px; width: 100%; display: flex; justify-content: center; gap: 9px; align-items: center; }
  .dot { width: 7px; height: 7px; border-radius: 50%; background: var(--dot); }
  .dot.active { width: 12px; height: 12px; background: none; border: 2px solid var(--dot); }
  .section-head {
    position: absolute; left: 50px; top: 864px; width: 1037px; display: flex; justify-content: space-between; align-items: baseline;
  }
  .section-head h2 { font-family: "Lora", serif; font-weight: 400; font-size: 29px; color: var(--ink); }
  .section-head a { font-family: "Arimo", sans-serif; font-size: 16px; color: var(--link); text-decoration: none; }
  .cards { position: absolute; left: 50px; top: 924px; display: flex; gap: 31px; }
  .card { width: 236px; height: 40px; border: 1px solid var(--card-line); border-bottom: none; padding: 18px 30px 0; }
  .card-photo { height: 22px; background: #b89a78; }
  .card:nth-child(2) .card-photo { background: #a9adb2; }
  .card:nth-child(3) .card-photo { background: #8d857d; margin: 0 40px; }
  .card:nth-child(4) .card-photo { background: #e6e1d6; }
</style>
</head>
<body>
<div class="page">
  <div class="brand">
    <div class="brand-square"></div>
    <div class="brand-name">Lanternfield Carpets<br>and Home</div>
  </div>

  <div class="account">
    <div><strong>Sign in</strong> &nbsp;or&nbsp; <strong>Create an Account</strong></div>
    <div>Call Toll-Free: <strong>1-888-555-MATS (6287)</strong></div>
  </div>

  <div class="search">
    <span>Search all products...</span>
    <svg width="20" height="20" viewBox="0 0 20 20" aria-hidden="true">
      <circle cx="8" cy="8" r="6" fill="none" stroke="#555" stroke-width="2"/>
      <line x1="12.5" y1="12.5" x2="18" y2="18" stroke="#555" stroke-width="2.4" stroke-linecap="round"/>
    </svg>
  </div>
  <div class="cart">
    <svg width="24" height="20" viewBox="0 0 24 20" aria-hidden="true">
      <path d="M1 2h4l3 11h12l2-8H7" fill="none" stroke="#555" stroke-width="1.6" stroke-linejoin="round"/>
      <circle cx="10" cy="17" r="1.6" fill="#555"/><circle cx="18" cy="17" r="1.6" fill="#555"/>
    </svg>
    <span>Cart</span>
  </div>

  <nav class="nav">
    <span>Rugs</span><span>Lighting</span><span>Pillows &amp; Poufs</span><span>Wall Decor</span>
    <span>Table Decor</span><span>Clearance</span><span>Contact Us</span>
  </nav>

  <section class="hero" role="img" aria-label="Faded tan rug pattern background with a Clearance Sale announcement">
    <div class="hero-title">Clearance Sale!</div>
    <div class="hero-sub"><span>✱</span>NOW IN PROGRESS<span>✱</span></div>
    <svg class="hero-rule" width="500" height="14" viewBox="0 0 500 14" aria-hidden="true">
      <path d="M2 8 Q250 2 498 6" fill="none" stroke="#ffffff" stroke-width="4" stroke-linecap="round"/>
    </svg>
  </section>

  <div class="dots">
    <div class="dot active"></div><div class="dot"></div><div class="dot"></div><div class="dot"></div>
  </div>

  <div class="section-head">
    <h2>Browse Categories</h2>
    <a href="#">More categories ›</a>
  </div>

  <div class="cards">
    <div class="card"><div class="card-photo" role="img" aria-label="Rug category photo"></div></div>
    <div class="card"><div class="card-photo" role="img" aria-label="Lighting category photo"></div></div>
    <div class="card"><div class="card-photo" role="img" aria-label="Wall decor category photo"></div></div>
    <div class="card"><div class="card-photo" role="img" aria-label="Pillows category photo"></div></div>
  </div>
</div>
</body>
</html>
```